Brightwell - Self Development Mobile App

Basic Instructions
1. please create an android app screen design for me, in figma, for my new app “Brightwell” based on this pencil drawing (Subjects.jpg)
2. Create the color pallet based on the colors of the logo (#fcd354 and #5dc9b7) and also add shades based on these colors based on material design.
3. the background should be white.
4. Use material design
Get Inspired by wordhopper design and calmnest design
These are the directions i provided for the programmer on how this screen will work:
top bar:
back icon on left (show if you are in a category and press to go back one category)
name of the field in middle in bold
share icon for sharing the current subject on the right before the drop down menu
3 dot icon on the right (drop down menu)
2nd top bar:
fire icon on left for streak (how many days straight did you do a lesson)
star icon a bit after it (how many lessons did you pass)
circles section:
each category will get a section
each category will have a small star with a number that shows how many stars the user has from that category
each category will have an icon before it
under each category there will be circles for all the subjects under that category
scroll horizontally to see more subjects
each subject will have the amount stars gained from it (like the circles of the fields in the fields screen)
scroll down to see more fields with their subjects
note that the order of the subjects and categories should be based on the practial/spiritual score that the user has been assigned based on the initial wizard
More Notes
1. the scribbles in the circles under the following categories (Dreams, Sub-Concious, Feeling)) are just place filers. Please add example content based on the content in the circles that are under “Memory” category
2. There are more sections after Feeling so users should be able to scroll down to see more sections
3. There are more categories to the right so under each section
Final Thoughts
Maybe its better to have rounded cornered squares instead of circles. You choose what you think is best.
After you have created the Subjects screen and I like it, then I'll give you instructions for the other 5 screens.
Target Market(s)
general public, adults 18-80
Font styles to use
Look and feel
Each slider illustrates characteristics of the customer's brand and the style your logo design should communicate.

```html
<!DOCTYPE html>
<html lang="en">
<head>
<meta charset="utf-8">
<title>Brightwell – Mind</title>
<link href="https://fonts.googleapis.com/css2?family=Poppins:wght@400;500;600&display=swap" rel="stylesheet">
<style>
:root{
  --stage:#e9eae9;
  --header:#eff8f6;
  --white:#ffffff;
  --ink:#111418;
  --muted:#a3a8b8;
  --gold:#fcd354;
  --gold-deep:#f5b91e;
  --teal:#5dc9b7;
  --teal-deep:#4aa394;
  --teal-ring:#e2f3f0;
  --blue:#5f86c9;
  --blue-ring:#e9eef8;
  --row-memory:#eef2fa;
  --row-dreams:#eef8f6;
  --row-sub:#f1fbf0;
  --row-feel:#fefbef;
  --row-thought:#fdf5f0;
  --row-affirm:#fdeef1;
}
*{box-sizing:border-box;margin:0;padding:0}
html,body{width:1200px;height:1100px;overflow:hidden;background:var(--stage);font-family:"Poppins",sans-serif;color:var(--ink)}
.screen{position:absolute;left:384px;top:70px;width:432px;height:960px;border-radius:44px;background:var(--header);overflow:hidden}
.sheet{position:absolute;left:0;top:137px;width:432px;height:823px;background:var(--white);border-top-right-radius:40px}
.abs{position:absolute}
.topbar-title{position:absolute;left:0;right:0;top:46px;text-align:center;font-weight:600;font-size:19px}
.icon{position:absolute}
.stats{position:absolute;left:16px;top:81px;width:152px;height:47px;border-radius:24px;background:var(--white);display:flex;align-items:center}
.stat{display:flex;align-items:center;gap:8px;padding:0 12px;color:var(--muted);font-size:17px;height:100%}
.stat + .stat{border-left:1.5px solid #eef1f1;padding-left:10px}
.category{position:absolute;left:16px;width:400px;height:56px;border-radius:28px;display:flex;align-items:center;padding-left:16px}
.category-name{margin-left:15px;font-weight:600;font-size:16px;letter-spacing:.2px}
.category-score{position:absolute;right:16px;display:flex;align-items:center;gap:10px;color:var(--muted);font-size:16px}
.memory{top:160px;background:var(--row-memory)}
.dreams{top:408px;background:var(--row-dreams)}
.subconscious{top:656px;background:var(--row-sub)}
.feelings{top:728px;background:var(--row-feel)}
.thoughts{top:800px;background:var(--row-thought)}
.affirmations{top:872px;background:var(--row-affirm)}
.subject{position:absolute;width:150px;height:150px;border-radius:50%;display:flex;align-items:center;justify-content:center}
.subject-art{position:absolute;left:7px;top:7px;width:136px;height:136px;border-radius:50%}
.subject-label{position:relative;text-align:center;color:var(--white);font-size:20px;line-height:20px}
.subject-stars{display:flex;align-items:center;justify-content:center;gap:6px;margin-top:8px;font-size:16px}
.memory-subject{background:var(--blue-ring)}
.memory-subject .subject-art{background:radial-gradient(circle at 50% 40%,#7b9ed6,var(--blue) 70%)}
.dream-subject{background:var(--teal-ring)}
.dream-subject .subject-art{background:radial-gradient(circle at 50% 45%,#5cb3a4,var(--teal-deep) 70%)}
.night .subject-art{background:radial-gradient(circle at 50% 50%,#6dd3c2 0,#52c0ad 56%,var(--teal-deep) 58%)}
.home-bar{position:absolute;left:138px;top:947px;width:154px;height:5px;border-radius:3px;background:var(--ink)}
</style>
</head>
<body>
<main class="screen">
  <svg class="icon" style="left:17px;top:50px" width="22" height="20" viewBox="0 0 22 20" fill="none" stroke="#111418" stroke-width="2.2" stroke-linecap="round" stroke-linejoin="round"><path d="M20 10H2M10 2 2 10l8 8"/></svg>
  <h1 class="topbar-title">Mind</h1>
  <svg class="icon" style="left:352px;top:48px" width="24" height="24" viewBox="0 0 24 24" fill="none" stroke="#111418" stroke-width="1.8"><circle cx="5" cy="12" r="3.2"/><circle cx="18" cy="5" r="3.2"/><circle cx="18" cy="19" r="3.2"/><path d="M8 10.5l7-4M8 13.5l7 4"/></svg>
  <svg class="icon" style="left:400px;top:49px" width="8" height="22" viewBox="0 0 8 22" fill="none" stroke="#111418" stroke-width="1.8"><circle cx="4" cy="3" r="2"/><circle cx="4" cy="11" r="2"/><circle cx="4" cy="19" r="2"/></svg>

  <div class="stats">
    <div class="stat">
      <svg width="22" height="26" viewBox="0 0 22 26"><path d="M11 1C7 6 1 10 1 16.5 1 22 5.5 25 11 25s10-3 10-8.5C21 10 15 6 11 1Z" fill="var(--teal)"/><path d="M11 13c-3 3-6 5-6 8 0 2.5 2.5 4 6 4s6-1.5 6-4c0-3-3-5-6-8Z" fill="#8ee0d2"/></svg>
      <span>20</span>
    </div>
    <div class="stat">
      <svg width="26" height="26" viewBox="0 0 24 24"><path d="M12 1.5l3.2 6.6 7.2 1-5.2 5 1.3 7.2L12 17.8 5.5 21.3l1.3-7.2-5.2-5 7.2-1z" fill="var(--gold)"/><path d="M12 1.5 15.2 8.1l7.2 1-5.2 5 1.3 7.2L12 17.8Z" fill="var(--gold-deep)"/></svg>
      <span>33</span>
    </div>
  </div>

  <section class="sheet">
    <div class="category memory" style="top:23px">
      <svg width="22" height="22" viewBox="0 0 24 24" fill="none" stroke="#111418" stroke-width="1.5"><rect x="2" y="2" width="15" height="20" rx="2"/><path d="M19 4l2.5 1.5-3 15"/><circle cx="7" cy="8" r="1.3"/><circle cx="11" cy="14" r="1.3"/><circle cx="8" cy="18" r="0.9"/></svg>
      <span class="category-name">Memory</span>
      <span class="category-score">7 <svg width="22" height="22" viewBox="0 0 24 24"><path d="M12 1.5l3.2 6.6 7.2 1-5.2 5 1.3 7.2L12 17.8 5.5 21.3l1.3-7.2-5.2-5 7.2-1z" fill="var(--gold-deep)"/></svg></span>
    </div>

    <div class="subject memory-subject" style="left:17px;top:88px"><div class="subject-art" role="img" aria-label="Photo of a memory card"></div><div class="subject-label">Basic<br>Memory<div class="subject-stars"><svg width="20" height="20" viewBox="0 0 24 24"><path d="M12 1.5l3.2 6.6 7.2 1-5.2 5 1.3 7.2L12 17.8 5.5 21.3l1.3-7.2-5.2-5 7.2-1z" fill="#e8eef8"/></svg>2</div></div></div>
    <div class="subject memory-subject" style="left:169px;top:88px"><div class="subject-art" role="img" aria-label="Photo of a handwritten name"></div><div class="subject-label">Names<div class="subject-stars"><svg width="20" height="20" viewBox="0 0 24 24"><path d="M12 1.5l3.2 6.6 7.2 1-5.2 5 1.3 7.2L12 17.8 5.5 21.3l1.3-7.2-5.2-5 7.2-1z" fill="#e8eef8"/></svg>1</div></div></div>
    <div class="subject memory-subject" style="left:321px;top:88px"><div class="subject-art" role="img" aria-label="Photo of large printed numbers"></div><div class="subject-label">Numbers<div class="subject-stars"><svg width="20" height="20" viewBox="0 0 24 24"><path d="M12 1.5l3.2 6.6 7.2 1-5.2 5 1.3 7.2L12 17.8 5.5 21.3l1.3-7.2-5.2-5 7.2-1z" fill="#e8eef8"/></svg>4</div></div></div>

    <div class="category dreams" style="top:271px">
      <svg width="22" height="22" viewBox="0 0 24 24" fill="none" stroke="#111418" stroke-width="1.7" stroke-linecap="round"><path d="M12 3a9 9 0 1 0 9 10.5A7 7 0 0 1 12 3Z"/><path d="M17 3v0M20 6v0M21 2v0"/></svg>
      <span class="category-name">Dreams</span>
      <span class="category-score">3 <svg width="22" height="22" viewBox="0 0 24 24"><path d="M12 1.5l3.2 6.6 7.2 1-5.2 5 1.3 7.2L12 17.8 5.5 21.3l1.3-7.2-5.2-5 7.2-1z" fill="var(--gold-deep)"/></svg></span>
    </div>

    <div class="subject dream-subject night" style="left:17px;top:336px"><div class="subject-art" role="img" aria-label="Photo of a full moon"></div><div class="subject-label">Night<br>Dreams<div class="subject-stars"><svg width="20" height="20" viewBox="0 0 24 24"><path d="M12 1.5l3.2 6.6 7.2 1-5.2 5 1.3 7.2L12 17.8 5.5 21.3l1.3-7.2-5.2-5 7.2-1z" fill="#e6f6f3"/></svg>2</div></div></div>
    <div class="subject dream-subject" style="left:169px;top:336px"><div class="subject-art" role="img" aria-label="Photo of a candle flame"></div><div class="subject-label">Bad<br>Dreams<div class="subject-stars"><svg width="20" height="20" viewBox="0 0 24 24"><path d="M12 1.5l3.2 6.6 7.2 1-5.2 5 1.3 7.2L12 17.8 5.5 21.3l1.3-7.2-5.2-5 7.2-1z" fill="#e6f6f3"/></svg>1</div></div></div>
    <div class="subject dream-subject" style="left:321px;top:336px"><div class="subject-art" role="img" aria-label="Photo of a sparkler"></div><div class="subject-label" style="margin-top:-8px">Day<br>Dreaming<div class="subject-stars" style="margin-top:4px"><svg width="20" height="20" viewBox="0 0 24 24"><path d="M12 1.5l3.2 6.6 7.2 1-5.2 5 1.3 7.2L12 17.8 5.5 21.3l1.3-7.2-5.2-5 7.2-1z" fill="#e6f6f3"/></svg>1</div></div></div>

    <div class="category subconscious" style="top:519px">
      <svg width="22" height="22" viewBox="0 0 24 24" fill="none" stroke="#111418" stroke-width="1.5"><circle cx="12" cy="12" r="10"/><path d="M12 5a7 7 0 0 0 0 14Z" fill="#c9cfcc"/></svg>
      <span class="category-name">Sub-conscious</span>
      <span class="category-score">12 <svg width="22" height="22" viewBox="0 0 24 24"><path d="M12 1.5l3.2 6.6 7.2 1-5.2 5 1.3 7.2L12 17.8 5.5 21.3l1.3-7.2-5.2-5 7.2-1z" fill="var(--gold-deep)"/></svg></span>
    </div>
    <div class="category feelings" style="top:591px">
      <svg width="22" height="22" viewBox="0 0 24 24" fill="none" stroke="#111418" stroke-width="1.5" stroke-linecap="round"><path d="M3 4c6 2 12 2 18 0v8a9 9 0 0 1-18 0Z"/><path d="M7 10q1.5-1 3 0M14 10q1.5-1 3 0M8 15q4 3 8 0"/></svg>
      <span class="category-name">Feelings</span>
      <span class="category-score">1 <svg width="22" height="22" viewBox="0 0 24 24"><path d="M12 1.5l3.2 6.6 7.2 1-5.2 5 1.3 7.2L12 17.8 5.5 21.3l1.3-7.2-5.2-5 7.2-1z" fill="var(--gold-deep)"/></svg></span>
    </div>
    <div class="category thoughts" style="top:663px">
      <svg width="22" height="22" viewBox="0 0 24 24" fill="none" stroke="#111418" stroke-width="1.5" stroke-linecap="round"><path d="M12 2a10 10 0 1 1-5 18.7L2 22l1.3-5A10 10 0 0 1 12 2Z"/><circle cx="14" cy="10" r="2.2"/><path d="M8 9v0M10 14v0"/></svg>
      <span class="category-name">Thoughts</span>
      <span class="category-score">5 <svg width="22" height="22" viewBox="0 0 24 24"><path d="M12 1.5l3.2 6.6 7.2 1-5.2 5 1.3 7.2L12 17.8 5.5 21.3l1.3-7.2-5.2-5 7.2-1z" fill="var(--gold-deep)"/></svg></span>
    </div>
    <div class="category affirmations" style="top:735px">
      <svg width="22" height="22" viewBox="0 0 24 24" fill="none" stroke="#111418" stroke-width="1.5" stroke-linecap="round"><circle cx="12" cy="11" r="9"/><path d="M4 17c2 4 14 4 16 0M10 9l3-3M9 13l5-5"/></svg>
      <span class="category-name">Affirmations</span>
      <span class="category-score">3 <svg width="22" height="22" viewBox="0 0 24 24"><path d="M12 1.5l3.2 6.6 7.2 1-5.2 5 1.3 7.2L12 17.8 5.5 21.3l1.3-7.2-5.2-5 7.2-1z" fill="var(--gold-deep)"/></svg></span>
    </div>
  </section>
  <div class="home-bar"></div>
</main>
</body>
</html>
```